Website for Corvalind Capital, my new firm that raises money from investors to buy, build, own an...

Corvalind Capital needs a website! We are a new company with very experienced people, who invest in, own and build hotel properties, as well as apartments and other commercial real estate. We seek investors for our projects, and we provide safe, secure returns on their investment in our projects. Our new logo is designed to exhibit strength, class and security, and would like our website to continue on this theme. Our name, Corvalind, is a word-play on a Greek word “aristeia”, which means “excellence” and “a warriors finest moment of glory in war”. If you are in business, you realize that much of it is like war, with strategy and moves and opponents and competitors, and ever-changing economic conditions and threats that make business very much like war. We like to think that we are good at business (war), and so have named our company “Corvalind”, using the founders last name and the word “aristeia” combined. Another definition of "aristeia" is "performing at the peak of one's potential after a long struggle"...again, much like business in real life! The website design should exhibit financial security, smart moves, and positive growth towards a bright future.

Target Market(s)

The target market is smart and wealthy investors, with others such as brokers, cities and government agencies, lenders, sellers, partners, etc also looking at it.

Industry/Entity Type

Investment

Number of Pages Required

5+ page

Font styles to use
Sans Serif

Colors
fec214

Requirements
Must have
• Our website should have a landing page, a "about" or bio page, a projects page and a contact us page. Our new logo uses the colors black and gold, so this should be factored in to our site. The site should be simple, yet impactful and impressive. I have actually two logos, which can be mixed and interchanged in a complimentary way, each with their own unique look.
Nice to have
• I have uploaded a couple screenshots of a website i like, and the simplicity I mention.
Should not have
• The site should not be flashy or complicated or complex or "busy"

```html
<!DOCTYPE html>
<html lang="en">
<head>
<meta charset="utf-8">
<title>Corvalind Capital</title>
<link href="https://fonts.googleapis.com/css2?family=Montserrat:wght@500;600;700&family=Lato:ital,wght@0,400;0,700;1,400;1,700&display=swap" rel="stylesheet">
<style>
:root{
  --gold:#c3942e;
  --black:#111111;
  --dark:#2b2b2b;
  --ink:#333333;
  --muted:#777777;
  --light:#f2f2f2;
  --white:#ffffff;
  --purple:#b43de0;
  --green:#2eaa4a;
  --orange:#f0582a;
}
*{margin:0;padding:0;box-sizing:border-box}
html,body{width:1200px;height:3333px;overflow:hidden}
body{position:relative;background:var(--white);font-family:'Lato',sans-serif;color:var(--ink)}
.abs{position:absolute}
.heading{font-family:'Montserrat',sans-serif;font-weight:700;color:var(--gold);letter-spacing:1px}
.photo{position:absolute}
.btn{position:absolute;display:flex;align-items:center;justify-content:center;gap:14px;font-family:'Lato',sans-serif;font-weight:700;font-size:19px;text-transform:uppercase;clip-path:polygon(6% 0,94% 0,100% 50%,94% 100%,6% 100%,0 50%)}
.btn-dark{background:var(--dark);color:var(--white)}
.btn-light{background:var(--white);color:var(--ink)}
.btn svg{width:38px;height:14px}

/* social links */
.social{position:absolute;z-index:5;width:50px;height:50px;border-radius:50%;background:var(--dark);color:var(--white);display:flex;align-items:center;justify-content:center;font-family:'Lato',sans-serif;font-weight:700;font-size:14px;box-shadow:0 0 0 3px rgba(255,255,255,.35)}
.social-light{background:var(--white);color:var(--ink);box-shadow:none}

/* top bar & header */
.topbar{top:0;left:0;width:1200px;height:40px;background:var(--gold)}
.topbar p{position:absolute;left:0;right:0;top:13px;text-align:center;font-size:12px;font-weight:700;color:var(--white)}
.header{top:40px;left:0;width:1200px;height:105px;background:var(--white)}
.brand{top:22px;left:78px;width:184px;height:145px;background:var(--black);display:flex;align-items:center;justify-content:center;z-index:3}
.brand span{font-weight:700;font-size:24px;color:var(--gold);letter-spacing:1px}
.nav{top:89px;left:398px;display:flex;gap:44px;font-size:17px;color:#555;text-transform:uppercase}
.nav .active{color:var(--gold);position:relative}
.nav .active::after{content:"";position:absolute;left:0;right:0;bottom:-45px;height:4px;background:var(--gold)}
.search{top:84px;left:862px;width:260px;height:38px;border:1px solid #ddd;border-radius:19px;background:#fafafa;font-size:13px;font-style:italic;color:#888;padding:11px 16px}
.search svg{position:absolute;right:14px;top:9px;width:19px;height:19px}

/* hero */
.hero{top:145px;left:0;width:1200px;height:573px;background:linear-gradient(180deg,#7d8fa6 0%,#5c6a7d 55%,#3c3f45 100%)}
.hero-panel{top:145px;left:393px;width:414px;height:573px;background:rgba(255,255,255,.28)}
.hero-title{top:282px;left:371px;width:458px;height:80px;background:var(--gold);display:flex;align-items:center;justify-content:center;font-family:'Montserrat',sans-serif;font-weight:500;font-size:44px;letter-spacing:6px;color:var(--white);text-transform:uppercase}
.hero-text{top:393px;left:405px;width:390px;text-align:center;font-size:15px;font-style:italic;font-weight:700;line-height:33px;color:#222}
.hero-cta{top:511px;left:371px;width:476px;height:62px;background:var(--black);color:var(--white);font-size:21px;font-weight:400;clip-path:polygon(0 0,96% 0,100% 50%,96% 100%,0 100%)}
.dots{top:650px;left:566px;display:flex;gap:8px;align-items:center}
.dots i{display:block;width:14px;height:14px;border-radius:50%;border:2px solid #333}
.dots i.on{background:var(--gold);border-color:var(--gold);width:18px;height:18px}

/* why */
.why{top:718px;left:0;width:1200px;height:666px;background:var(--light)}
.section-title{position:absolute;left:0;width:1200px;text-align:center;font-size:34px}
.rule{position:absolute;left:573px;width:54px;height:3px;background:#555}
.why-card{top:927px;left:184px;width:832px;height:373px;background:var(--white);border-radius:30px;box-shadow:0 6px 24px rgba(0,0,0,.12)}
.feature-icon{position:absolute;width:86px;height:86px;border-radius:50%;display:flex;align-items:center;justify-content:center;box-shadow:0 0 0 5px rgba(0,0,0,.06)}
.feature-icon svg{width:40px;height:40px}
.feature-name{position:absolute;font-size:20px;font-weight:400}
.feature-text{position:absolute;font-size:14px;line-height:26px;color:var(--muted);width:250px}

/* about */
.about{top:1384px;left:0;width:600px;height:416px;background:var(--gold)}
.about-title{top:1437px;left:78px;font-family:'Montserrat',sans-serif;font-weight:700;font-size:36px;color:var(--white)}
.about-text{top:1512px;left:78px;width:460px;font-size:14px;line-height:24px;color:var(--white)}

/* hire */
.hire{top:2467px;left:0;width:1200px;height:249px;background:var(--gold)}
.hire-title{top:2527px;left:78px;font-family:'Montserrat',sans-serif;font-weight:700;font-size:35px;color:var(--white);letter-spacing:1px}
.hire-text{top:2585px;left:78px;width:780px;font-size:14px;line-height:26px;color:var(--white)}

/* contact */
.contact-title{font-size:31px}
.info-icon{position:absolute;left:207px;width:44px;height:44px;border-radius:50%;background:#f7f0e2;display:flex;align-items:center;justify-content:center}
.info-icon svg{width:22px;height:22px}
.info-line{position:absolute;left:78px;width:302px;text-align:center;font-size:15px;line-height:27px;color:var(--ink)}
.msg-text{top:2852px;left:442px;width:600px;font-size:14px;line-height:28px;color:#555}
.field{position:absolute;height:60px;border:1px solid #ddd;background:linear-gradient(#fbfbfb,#f0f0f0);font-size:13px;color:#555;padding:14px 12px}

/* footer */
.footer{top:3249px;left:0;width:1200px;height:84px;background:var(--gold)}
.copyright{top:3283px;left:78px;font-size:13px;color:var(--white)}
</style>
</head>
<body>

<div class="abs topbar"><p>Welcome to CORVALIND CAPITAL....!</p></div>
<header class="abs header"></header>
<span class="social" style="top:16px;left:946px">Vx</span>
<span class="social" style="top:16px;left:1008px">Pn</span>
<span class="social" style="top:16px;left:1071px">Fd</span>

<div class="abs brand"><span>CORVALIND</span></div>
<nav class="abs nav">
  <span class="active">Home</span><span>About</span><span>Projects</span><span>Contact</span>
</nav>
<div class="abs search">Search here.....
  <svg viewBox="0 0 20 20" fill="none" stroke="#c3942e" stroke-width="2"><circle cx="8" cy="8" r="6"/><path d="M12.5 12.5 18 18"/></svg>
</div>

<section class="abs hero" role="img" aria-label="Modern office building at dusk"></section>
<div class="abs hero-panel"></div>
<div class="abs hero-title">Corvalind</div>
<p class="abs hero-text">Lorem Ipsum is simply dummy text of the printing and typesetting industry. Lorem Ipsum has been the industry's standard dummy text ever since the 1500s,</p>
<div class="btn hero-cta">Contact us
  <svg viewBox="0 0 38 14" fill="none" stroke="#fff" stroke-width="2"><path d="M0 7h36M30 1l6 6-6 6"/></svg>
</div>
<div class="abs dots"><i></i><i class="on"></i><i></i></div>

<section class="abs why"></section>
<h2 class="heading section-title" style="top:778px">WHY CHOOSE US</h2>
<span class="rule" style="top:827px"></span>
<div class="abs why-card"></div>
<div class="photo" role="img" aria-label="Smiling businesswoman holding a tablet" style="top:840px;left:222px;width:345px;height:460px;background:linear-gradient(180deg,#e8e4df 0%,#cfc6bc 50%,#bdb4aa 100%);border-radius:170px 170px 0 0"></div>

<div class="feature-icon" style="top:950px;left:597px;background:var(--purple)">
  <svg viewBox="0 0 40 40" fill="none" stroke="#fff" stroke-width="2"><rect x="10" y="8" width="20" height="26"/><path d="M15 14h3M22 14h3M15 20h3M22 20h3M15 26h3M22 26h3M6 34h28"/></svg>
</div>
<h3 class="feature-name" style="top:954px;left:711px;color:var(--purple)">Build Hotel Properties</h3>
<p class="feature-text" style="top:988px;left:711px">Lorem Ipsum is simply dummy text of the printing and typesetting industry.</p>

<div class="feature-icon" style="top:1064px;left:597px;background:var(--green)">
  <svg viewBox="0 0 40 40" fill="none" stroke="#fff" stroke-width="2"><rect x="9" y="6" width="22" height="28"/><path d="M14 12h4M22 12h4M14 18h4M22 18h4M14 24h4M22 24h4M18 34v-5h4v5"/></svg>
</div>
<h3 class="feature-name" style="top:1068px;left:711px;color:var(--green)">Build Apartments</h3>
<p class="feature-text" style="top:1102px;left:711px">Lorem Ipsum is simply dummy text of the printing and typesetting industry.</p>

<div class="feature-icon" style="top:1179px;left:597px;background:var(--orange)">
  <svg viewBox="0 0 40 40" fill="none" stroke="#fff" stroke-width="2"><path d="M6 20 20 8l14 12M10 17v16h20V17M17 33v-9h6v9"/></svg>
</div>
<h3 class="feature-name" style="top:1183px;left:711px;color:var(--orange)">Commercial Real Estate</h3>
<p class="feature-text" style="top:1217px;left:711px">Lorem Ipsum is simply dummy text of the printing and typesetting industry.</p>

<section class="abs about"></section>
<div class="photo" role="img" aria-label="Two businessmen talking in front of a city skyline" style="top:1384px;left:600px;width:600px;height:416px;background:linear-gradient(135deg,#d9dde3 0%,#9aa3ae 45%,#3d4450 100%)"></div>
<h2 class="abs about-title">ABOUT US</h2>
<p class="abs about-text">Lorem Ipsum is simply dummy text of the printing and typesetting industry. Lorem Ipsum has been the industry's standard dummy text ever since the 1500s, when an unknown printer took a galley of type and scrambled it to make a type specimen book. It has survived not only five centuries, but also the leap into electronic typesetting, remaining essentially unchanged.</p>
<div class="btn btn-light" style="top:1689px;left:78px;width:206px;height:49px">Read more
  <svg viewBox="0 0 38 14" fill="none" stroke="#333" stroke-width="2"><path d="M0 7h36M30 1l6 6-6 6"/></svg>
</div>

<h2 class="heading section-title" style="top:1860px">OUR PROJECTS</h2>
<span class="rule" style="top:1909px"></span>
<div class="photo" role="img" aria-label="Business partners meeting at a table" style="top:2040px;left:78px;width:249px;height:189px;background:linear-gradient(135deg,#d7dade,#8a8f96)"></div>
<div class="photo" role="img" aria-label="Team reviewing a tablet in an office" style="top:1949px;left:344px;width:249px;height:362px;background:linear-gradient(180deg,#c5cbd1,#5a5f66)"></div>
<div class="photo" role="img" aria-label="Colleagues celebrating with a high five" style="top:1949px;left:607px;width:249px;height:173px;background:linear-gradient(135deg,#e6e2dc,#9c958d)"></div>
<div class="photo" role="img" aria-label="Team working at laptops" style="top:2138px;left:607px;width:249px;height:173px;background:linear-gradient(135deg,#eef0f2,#a6aab0)"></div>
<div class="photo" role="img" aria-label="Two people in a relaxed office meeting" style="top:2022px;left:871px;width:251px;height:227px;background:linear-gradient(135deg,#ddd6d4,#8f7f7c)"></div>
<div class="btn btn-dark" style="top:2355px;left:518px;width:204px;height:49px">Read more
  <svg viewBox="0 0 38 14" fill="none" stroke="#fff" stroke-width="2"><path d="M0 7h36M30 1l6 6-6 6"/></svg>
</div>

<section class="abs hire"></section>
<h2 class="abs hire-title">HIRE ME FOR YOUR AWESOME PROJECT</h2>
<p class="abs hire-text">Lorem Ipsum is simply dummy text of the printing and typesetting industry. Lorem Ipsum has been the industry's standard dummy text ever since the 1500s, when an unknown printer took a galley of type and scrambled it to make a type specimen book.</p>
<div class="btn btn-dark" style="top:2531px;left:907px;width:215px;height:51px">Get a quote
  <svg viewBox="0 0 38 14" fill="none" stroke="#fff" stroke-width="2"><path d="M0 7h36M30 1l6 6-6 6"/></svg>
</div>

<h2 class="heading abs contact-title" style="top:2771px;left:78px">CONTACT INFO</h2>
<div class="info-icon" style="top:2854px">
  <svg viewBox="0 0 22 22" fill="#c3942e"><path d="M11 1a7 7 0 0 0-7 7c0 5 7 13 7 13s7-8 7-13a7 7 0 0 0-7-7zm0 10a3 3 0 1 1 0-6 3 3 0 0 1 0 6z"/></svg>
</div>
<p class="info-line" style="top:2912px">123, Address, State, City,<br>Street, Zipcode.</p>
<div class="info-icon" style="top:2989px">
  <svg viewBox="0 0 22 22" fill="#c3942e"><path d="M5 2l4 4-2 3c1 2 3 4 6 6l3-2 4 4-3 3C9 20 2 13 2 5z"/></svg>
</div>
<p class="info-line" style="top:3046px;font-weight:700">+1 234 567 8900</p>
<div class="info-icon" style="top:3102px">
  <svg viewBox="0 0 22 22" fill="none" stroke="#c3942e" stroke-width="2"><rect x="2" y="5" width="18" height="13"/><path d="M2 5l9 7 9-7"/></svg>
</div>
<p class="info-line" style="top:3159px;font-weight:700">info@corvalindcapital.com</p>

<h2 class="heading abs contact-title" style="top:2771px;left:442px">SENA YOUR MESSAGE</h2>
<p class="abs msg-text">Lorem Ipsum is simply dummy text of the printing and typesetting industry. Lorem Ipsum has been the industry's standard dummy text ever since the 1500s.</p>
<div class="field" style="top:2927px;left:442px;width:211px">Name :</div>
<div class="field" style="top:2927px;left:676px;width:211px">Name :</div>
<div class="field" style="top:2927px;left:909px;width:213px">Name :</div>
<div class="field" style="top:3009px;left:442px;width:680px;height:102px">Message / Comments :</div>
<div class="btn btn-dark" style="top:3135px;left:442px;width:216px;height:49px">Get a quote
  <svg viewBox="0 0 38 14" fill="none" stroke="#fff" stroke-width="2"><path d="M0 7h36M30 1l6 6-6 6"/></svg>
</div>

<footer class="abs footer"></footer>
<p class="abs copyright">Copyright © <b>CORVALIND CAPITAL</b> - 2018. All Right Reserved</p>
<span class="social social-light" style="top:3266px;left:946px">Vx</span>
<span class="social social-light" style="top:3266px;left:1008px">Pn</span>
<span class="social social-light" style="top:3266px;left:1071px">Fd</span>

</body>
</html>
```